Business Card Design for Online Gift Business

Business card design for a new online Canadian company called "Hale & Brook Gift Boxes" selling modern and luxurious gift boxes for every occasion. Items are sourced locally from talented socially-responsible Canadian artisans. Each gift is elegantly presented in a keepsake wood box to ensure a lasting impression.

Industry/Entity Type

E-Commerce

Contact Information for Business Card

Marla Pendleton, Proprietor
Kelowna, BC
250-555-2741
www.haleandbrook.ca
hello@haleandbrook.ca

Requirements
Must have
• Gifts from our makers, to your door
• Please also include the symbols for Facebook and Instagram
Nice to have
• **I have attached a few samples of background colors and font colors that I like. I hope this helps in a few directions to try.

```html
<!DOCTYPE html>
<html lang="en">
<head>
<meta charset="utf-8">
<title>Hale &amp; Brook Gift Boxes – Business Card</title>
<link href="https://fonts.googleapis.com/css2?family=EB+Garamond:wght@400;500&family=Italianno&display=swap" rel="stylesheet">
<style>
  :root {
    --backdrop: #8c8c8c;
    --card-dark: #1f1f1f;
    --card-light: #ffffff;
    --ink-light: #f4f4f4;
    --gold: #b39c73;
    --gold-line: #cdbb98;
  }
  * { box-sizing: border-box; margin: 0; padding: 0; }
  html, body {
    width: 900px;
    height: 1200px;
    overflow: hidden;
    background: var(--backdrop);
  }
  .canvas {
    position: relative;
    width: 900px;
    height: 1200px;
  }
  .card {
    position: absolute;
    left: 170px;
    width: 560px;
    height: 320px;
    box-shadow: 0 10px 24px rgba(0,0,0,0.28);
  }
  /* Front */
  .card-front {
    top: 190px;
    background: var(--card-dark);
    color: var(--ink-light);
    display: flex;
    flex-direction: column;
    align-items: center;
    justify-content: center;
    gap: 30px;
  }
  .brand-name {
    font-family: "EB Garamond", serif;
    font-weight: 400;
    font-size: 58px;
    letter-spacing: 2px;
    color: var(--ink-light);
    line-height: 1;
  }
  .tagline {
    font-family: "EB Garamond", serif;
    font-size: 19px;
    color: var(--ink-light);
  }
  /* Back */
  .card-back {
    top: 650px;
    background: var(--card-light);
  }
  .brand-mark {
    position: absolute;
    left: 92px;
    top: 110px;
    width: 100px;
    height: 100px;
    border-radius: 50%;
    background: var(--gold);
  }
  .divider {
    position: absolute;
    left: 262px;
    top: 80px;
    width: 1px;
    height: 160px;
    background: var(--gold-line);
  }
  .contact {
    position: absolute;
    left: 290px;
    top: 90px;
    color: var(--gold);
    font-family: "EB Garamond", serif;
  }
  .contact-name {
    font-family: "Italianno", cursive;
    font-size: 34px;
    line-height: 1;
  }
  .contact-role {
    font-size: 14px;
    margin: 2px 0 8px;
  }
  .contact-list { list-style: none; }
  .contact-item {
    display: flex;
    align-items: center;
    gap: 8px;
    font-size: 14px;
    line-height: 20px;
  }
  .contact-icon {
    width: 13px;
    height: 13px;
    flex: none;
  }
  .social {
    position: absolute;
    right: 26px;
    bottom: 22px;
    display: flex;
    align-items: center;
    gap: 5px;
    color: var(--gold);
    font-family: "EB Garamond", serif;
    font-size: 13px;
  }
  .social-label { margin-right: 4px; }
  .social-dot {
    width: 10px;
    height: 10px;
    border-radius: 50%;
    background: var(--gold);
  }
</style>
</head>
<body>
<main class="canvas">
  <section class="card card-front" aria-label="Business card front">
    <h1 class="brand-name">Hale &amp; Brook</h1>
    <p class="tagline">Gifts from our makers, to your door</p>
  </section>

  <section class="card card-back" aria-label="Business card back">
    <div class="brand-mark" aria-hidden="true"></div>
    <div class="divider" aria-hidden="true"></div>
    <div class="contact">
      <p class="contact-name">Marla Pendleton</p>
      <p class="contact-role">Proprietor</p>
      <ul class="contact-list">
        <li class="contact-item">
          <svg class="contact-icon" viewBox="0 0 14 14" aria-hidden="true"><rect width="14" height="14" rx="2" fill="#b39c73"/><path d="M7 3a2.6 2.6 0 0 0-2.6 2.6C4.4 7.6 7 11 7 11s2.6-3.4 2.6-5.4A2.6 2.6 0 0 0 7 3zm0 3.6a1 1 0 1 1 0-2 1 1 0 0 1 0 2z" fill="#fff"/></svg>
          Kelowna, BC
        </li>
        <li class="contact-item">
          <svg class="contact-icon" viewBox="0 0 14 14" aria-hidden="true"><rect width="14" height="14" rx="2" fill="#b39c73"/><path d="M4.3 3.2l1.4-.2.9 2-.9.8a5 5 0 0 0 2.5 2.5l.8-.9 2 .9-.2 1.4c-.1.5-.6.8-1.1.7A7 7 0 0 1 3.6 4.3c-.1-.5.2-1 .7-1.1z" fill="#fff"/></svg>
          250-555-2741
        </li>
        <li class="contact-item">
          <svg class="contact-icon" viewBox="0 0 14 14" aria-hidden="true"><rect width="14" height="14" rx="2" fill="#b39c73"/><rect x="3" y="4.2" width="8" height="5.6" rx=".6" fill="#fff"/><path d="M3.3 4.6L7 7.4l3.7-2.8" stroke="#b39c73" stroke-width=".9" fill="none"/></svg>
          hello@haleandbrook.ca
        </li>
        <li class="contact-item">
          <svg class="contact-icon" viewBox="0 0 14 14" aria-hidden="true"><rect width="14" height="14" rx="2" fill="#b39c73"/><circle cx="7" cy="7" r="3.6" stroke="#fff" stroke-width="1" fill="none"/><path d="M3.4 7h7.2M7 3.4c-1.6 2-1.6 5.2 0 7.2M7 3.4c1.6 2 1.6 5.2 0 7.2" stroke="#fff" stroke-width=".8" fill="none"/></svg>
          haleandbrook.ca
        </li>
      </ul>
    </div>
    <div class="social">
      <span class="social-label">Find us on</span>
      <span class="social-dot" aria-label="Social page"></span>
      <span class="social-dot" aria-label="Photo page"></span>
      <span class="social-dot" aria-label="Website"></span>
    </div>
  </section>
</main>
</body>
</html>
```